Flyer for our prophetic church event

I need a flyer designed for the launching of our "Nine Radiant Lord's Day Gatherings" event. This event should high light the next 7 Sundays starting on February the 11th, 2018

Event Name:
Nine Radiant Lord's Days

Event Slogan or topic:
Go and tell John ... the blind see, the lame walk, the lepers are cleansed, the deaf hear, the dead are raised,
the poor have the gospel preached to them.

Speaker:
Prophet Tomas Okello

February 11th
February 18th
February 25th
March 4th
March 11th
March 18th
March 25th

Location:
Halvor Community Center
382 Wendle Street
Portland, ME 04102
United States

Time:
10:00AM - 12:00PM

We welcome you all in the name of Jesus Christ

Contact Info:
Tel:+1(207) 555 3184 - Email:contact@brightmeadowfold.org - Website: http://velkor.org

Target Market(s)

Young adults

Industry/Entity Type

Church

Font styles to use
Other font styles liked:
• Surprise me, I trust the designers skills

Colors

Designer to choose colors to be used in the design.

Requirements
Must have
• The Velkor logo
• Tomas Okello's picture
• The
Should not have
• The background of the Tomas Okello's picture

```html
<!DOCTYPE html>
<html lang="en">
<head>
<meta charset="utf-8">
<title>Nine Radiant Lord's Days – Velkor</title>
<link rel="stylesheet" href="https://fonts.googleapis.com/css2?family=Raleway:wght@500;600;700;800&family=Lobster&display=swap">
<style>
:root{
  --blue:#0c4a7d;
  --blue-deep:#083a64;
  --orange:#f28a1c;
  --ink:#3a3a3a;
  --panel:#f2f2f2;
  --bar:#dcdcdc;
  --white:#ffffff;
}
*{margin:0;padding:0;box-sizing:border-box}
html,body{width:999px;height:1200px;overflow:hidden;background:var(--white)}
body{font-family:"Raleway",sans-serif;color:var(--blue)}
.flyer{position:relative;width:999px;height:1200px;overflow:hidden;background:var(--white)}

.brand{position:absolute;left:70px;top:56px;display:flex;align-items:center;gap:12px}
.brand-dot{width:26px;height:26px;border-radius:50%;background:var(--orange)}
.brand-name{font-size:56px;font-weight:600;letter-spacing:2px;color:var(--blue);line-height:1}

.title{position:absolute;left:66px;top:180px;display:flex;align-items:center;gap:14px;white-space:nowrap}
.title-number{font-size:78px;font-weight:800;color:var(--orange);line-height:1}
.title-script{font-family:"Lobster",cursive;font-size:44px;color:var(--blue);line-height:1.08}

.start{position:absolute;left:72px;top:360px}
.start-line{font-size:28px;font-weight:700;color:var(--blue)}
.start-date{font-size:40px;font-weight:800;color:var(--orange);margin-top:4px}
.start-date sup{font-size:20px}

.speaker-photo{position:absolute;left:560px;top:70px;width:439px;height:560px;
  background:radial-gradient(ellipse at 50% 30%,#5b4336 0%,#2b2b2f 45%,#1b1d22 80%,#2b2b2f 100%)}

.band{position:absolute;left:0;top:0;width:999px;height:1200px}

.venue{position:absolute;left:60px;top:560px;color:var(--white)}
.venue-row{display:flex;gap:14px;align-items:flex-start}
.venue-name{font-size:18px;font-weight:800;letter-spacing:.3px}
.venue-address{font-size:17px;font-weight:500;line-height:1.4}
.time{position:absolute;left:60px;top:648px;display:flex;align-items:center;gap:14px;color:var(--white);font-size:24px;font-weight:800}
.speaker{position:absolute;right:70px;top:590px;color:var(--white);font-size:22px;font-weight:600}
.speaker strong{color:var(--orange);font-weight:800}

.dates{position:absolute;left:560px;top:720px;width:439px;height:360px;background:var(--panel);border-top-left-radius:60px}
.dates-title{font-size:26px;font-weight:700;color:var(--blue);text-align:center;margin-top:26px;margin-bottom:14px}
.dates-list{list-style:none}
.dates-list li{width:240px;margin:0 auto;height:36px;line-height:36px;text-align:center;font-size:22px;font-weight:700;color:var(--ink)}
.dates-list li:nth-child(odd){background:var(--bar)}
.dates-list sup{font-size:11px}

.message{position:absolute;left:60px;top:770px;width:480px}
.message-title{font-size:26px;font-weight:700;color:var(--blue);margin-bottom:18px}
.checks{list-style:none;display:grid;grid-template-columns:auto auto;gap:10px 34px;justify-content:start}
.checks li{display:flex;align-items:center;gap:10px;font-size:17px;font-weight:600;color:var(--ink)}
.checks li.wide{grid-column:1 / 3}

.welcome{position:absolute;left:60px;top:970px;font-size:30px;font-weight:700;color:var(--ink);line-height:1.25}
.welcome-top{text-transform:uppercase}
.welcome em{font-style:normal;color:var(--orange);text-transform:uppercase}

.footer{position:absolute;left:0;bottom:0;width:999px;height:120px}
.contact{position:absolute;left:70px;bottom:28px;display:flex;align-items:flex-end;gap:26px;color:var(--white);white-space:nowrap}
.contact-lead{font-size:20px;font-weight:700;line-height:1.3}
.contact-lead .contact-item{display:inline-flex;margin-left:8px;vertical-align:middle}
.contact-item{display:flex;align-items:center;gap:7px;font-size:15px;font-weight:600;white-space:nowrap}
</style>
</head>
<body>
<main class="flyer">

  <div class="brand">
    <span class="brand-dot"></span>
    <span class="brand-name">VELKOR</span>
  </div>

  <div class="title">
    <span class="title-number">Nine</span>
    <span class="title-script">Radiant<br>Lord's Days</span>
  </div>

  <div class="start">
    <p class="start-line">Starting on February</p>
    <p class="start-date">THE 11<sup>TH</sup>, 2018</p>
  </div>

  <div class="speaker-photo" role="img" aria-label="Portrait of speaker Tomas Okello in a dark blazer and light blue shirt, background removed"></div>

  <svg class="band" viewBox="0 0 999 1200" aria-hidden="true">
    <path d="M0 520 Q40 490 130 492 L999 560 L999 574 L130 506 Q50 504 0 534 Z" fill="var(--orange)"/>
    <path d="M0 534 Q50 504 130 506 L999 574 L999 700 Q980 650 920 648 L0 720 Z" fill="var(--blue)"/>
    <path d="M0 720 L920 648 Q960 648 975 665 L0 734 Z" fill="var(--orange)"/>
  </svg>

  <div class="venue">
    <div class="venue-row">
      <svg width="24" height="32" viewBox="0 0 24 32" aria-hidden="true"><path d="M12 2a9 9 0 0 0-9 9c0 7 9 16 9 16s9-9 9-16a9 9 0 0 0-9-9z" fill="none" stroke="var(--orange)" stroke-width="2.5"/><circle cx="12" cy="11" r="3.5" fill="none" stroke="var(--orange)" stroke-width="2.5"/><path d="M4 30h16" stroke="var(--orange)" stroke-width="2.5"/></svg>
      <div>
        <p class="venue-name">HALVOR COMMUNITY CENTER</p>
        <p class="venue-address">382 Wendle Street,<br>Portland, ME 04102, United States</p>
      </div>
    </div>
  </div>

  <div class="time">
    <svg width="30" height="30" viewBox="0 0 30 30" aria-hidden="true"><circle cx="15" cy="15" r="12.5" fill="none" stroke="var(--orange)" stroke-width="2.5"/><path d="M15 8v7l5 4" fill="none" stroke="var(--orange)" stroke-width="2.5" stroke-linecap="round"/></svg>
    <span>10:00AM - 12:00PM</span>
  </div>

  <p class="speaker">Speaker: <strong>TOMAS</strong> OKELLO</p>

  <section class="dates">
    <h2 class="dates-title">Event Dates:</h2>
    <ul class="dates-list">
      <li>11<sup>TH</sup> February</li>
      <li>18<sup>TH</sup> February</li>
      <li>25<sup>TH</sup> February</li>
      <li>4<sup>TH</sup> March</li>
      <li>11<sup>TH</sup> March</li>
      <li>18<sup>TH</sup> March</li>
      <li>25<sup>TH</sup> March</li>
    </ul>
  </section>

  <section class="message">
    <h2 class="message-title">Go and tell John ...</h2>
    <ul class="checks">
      <li><svg width="16" height="16" viewBox="0 0 16 16" aria-hidden="true"><rect x="1" y="3" width="12" height="12" fill="none" stroke="var(--blue)" stroke-width="1.6"/><path d="M4 8l3 3 8-9" fill="none" stroke="var(--blue)" stroke-width="1.6"/></svg>The blind see</li>
      <li><svg width="16" height="16" viewBox="0 0 16 16" aria-hidden="true"><rect x="1" y="3" width="12" height="12" fill="none" stroke="var(--blue)" stroke-width="1.6"/><path d="M4 8l3 3 8-9" fill="none" stroke="var(--blue)" stroke-width="1.6"/></svg>The lame walk</li>
      <li class="wide"><svg width="16" height="16" viewBox="0 0 16 16" aria-hidden="true"><rect x="1" y="3" width="12" height="12" fill="none" stroke="var(--blue)" stroke-width="1.6"/><path d="M4 8l3 3 8-9" fill="none" stroke="var(--blue)" stroke-width="1.6"/></svg>The lepers are cleansed</li>
      <li><svg width="16" height="16" viewBox="0 0 16 16" aria-hidden="true"><rect x="1" y="3" width="12" height="12" fill="none" stroke="var(--blue)" stroke-width="1.6"/><path d="M4 8l3 3 8-9" fill="none" stroke="var(--blue)" stroke-width="1.6"/></svg>The deaf hear</li>
      <li><svg width="16" height="16" viewBox="0 0 16 16" aria-hidden="true"><rect x="1" y="3" width="12" height="12" fill="none" stroke="var(--blue)" stroke-width="1.6"/><path d="M4 8l3 3 8-9" fill="none" stroke="var(--blue)" stroke-width="1.6"/></svg>The dead are raised</li>
      <li class="wide"><svg width="16" height="16" viewBox="0 0 16 16" aria-hidden="true"><rect x="1" y="3" width="12" height="12" fill="none" stroke="var(--blue)" stroke-width="1.6"/><path d="M4 8l3 3 8-9" fill="none" stroke="var(--blue)" stroke-width="1.6"/></svg>The poor have the gospel preached to them.</li>
    </ul>
  </section>

  <p class="welcome"><span class="welcome-top">We welcome you all in</span><br>The name of <em>Jesus Christ</em></p>

  <svg class="footer" viewBox="0 0 999 120" aria-hidden="true">
    <path d="M120 4 L999 0 L999 8 L120 12 Z" fill="var(--orange)"/>
    <path d="M0 120 L0 90 Q20 18 110 16 L999 12 L999 120 Z" fill="var(--blue)"/>
  </svg>

  <div class="contact">
    <p class="contact-lead">For Registration or more details<br>CONTACT US :
      <span class="contact-item"><svg width="16" height="16" viewBox="0 0 16 16" aria-hidden="true"><path d="M3 1l3 3-2 2c1 2 3 4 5 5l2-2 3 3-2 3C7 15 1 9 1 3z" fill="var(--orange)"/></svg>+1(207) 555 3184</span>
    </p>
    <span class="contact-item"><svg width="18" height="18" viewBox="0 0 18 18" aria-hidden="true"><circle cx="9" cy="9" r="7.5" fill="none" stroke="var(--orange)" stroke-width="1.6"/><ellipse cx="9" cy="9" rx="3.2" ry="7.5" fill="none" stroke="var(--orange)" stroke-width="1.4"/><path d="M1.5 9h15" stroke="var(--orange)" stroke-width="1.4"/></svg>www.velkor.org</span>
    <span class="contact-item"><svg width="20" height="14" viewBox="0 0 20 14" aria-hidden="true"><rect x="1" y="1" width="18" height="12" fill="none" stroke="var(--orange)" stroke-width="1.6"/><path d="M1 1l9 7 9-7" fill="none" stroke="var(--orange)" stroke-width="1.6"/></svg>contact@brightmeadowfold.org</span>
  </div>

</main>
</body>
</html>
```